Vision Board to graphically depict our Vision to a larger audience

We currently use a simplistic graphic, created internally, to depict our vision. We want to expand that to show the depth of what we want to connect, who we want to connect, and how we want to connect. Our vision statement is "to connect resources for at-risk populations through other nonprofits, businesses, and schools, in a way that empowers rather than enables. Resources to be connected are people, products, and meaningful purpose. (at-risk populations refers to low income people who can be homelesses, under educated, under employed, senior citizens, refugees, foster care, single teen parents etc.) The businesses we want to connect refer to businesses who want to have a "social footprint" by being known for donating to specific causes. (Pello shoes sells a pair and donates a pair, vindle socks does something similar). We want to show that by utilizing our nonprofit warehouse to donate products to, we can help build your business by letting potential shoppers know that you support at-risk people through our organization. In addition the full circle we want to show in this visual is that the people being helped by getting products and services, end up healthier and ready to be employed by the very businesses who have donated.

Target Market(s)

Business to Business (Target will be other nonprofits who will want to come and shop from our warehouse and take goods on behalf of the low-income people they work with as well as connect to other like minded nonprofits- i.e housing orgs. connect, work force development groups connect etc). Target- Businesses who have goods they can donate to have a social impact as well as donate services and/or employee at-risk people. Target- Populations of people (especially senior citizens or stay at home parents) who have talents to give and looking for an avenue to use them for social good (as a volunteer).

Industry/Entity Type

Non Profit

Font styles to use
Sans Serif

Colors

Designer to choose colors to be used in the design.

Requirements
Must have
• Must have our name and logo. Must show how we connect each piece of the puzzle. Sponsors donate and are critical but ultimately we are trying to develop relationships with local businesses who will be the new donors/sponsors. I love pictures to depict messages as much as possible. I would prefer to have the nonprofit names listed and/or the logo of the organization.
Nice to have
• I have thought of depicting this as a wheel with The Larderwell in the center almost like a Venn Diagram but it never seems to fully explain what we are doing. Ultimately the biggest challenge is showing that the person being impacted is the "low income/at-risk person" even though the "clients" who shop are "nonprofit businesses" and the donors are "for profit businesses".

```html
<!DOCTYPE html>
<html lang="en">
<head>
<meta charset="utf-8">
<title>The Larderwell – Vision Board</title>
<link rel="stylesheet" href="https://fonts.googleapis.com/css2?family=Saira+Semi+Condensed:wght@700;800&family=Source+Serif+4:ital,wght@0,400;1,700&display=swap">
<style>
  :root {
    --green: #7ab648;
    --ink: #3d3d3d;
    --text: #1a1a1a;
    --paper: #ffffff;
    --icon-dark: #111111;
    --icon-blue: #4a76a8;
    --icon-store: #3c78d0;
  }
  html, body {
    margin: 0;
    width: 1200px;
    height: 840px;
    overflow: hidden;
    background: var(--paper);
  }
  .vision-board { display: block; width: 1200px; height: 840px; }
  .node-ring { fill: var(--paper); stroke: var(--green); stroke-width: 5; }
  .flow-gap { fill: none; stroke: var(--paper); stroke-width: 74; stroke-linejoin: round; }
  .flow-rail { stroke: var(--green); stroke-width: 6; stroke-linecap: butt; }
  .flow-path { fill: none; stroke: var(--ink); stroke-width: 7; stroke-linejoin: miter; }
  .flow-head { fill: var(--ink); }
  .note-arrow { stroke: var(--ink); stroke-width: 5; }
  .brand-name { font-family: "Saira Semi Condensed", sans-serif; font-weight: 800; fill: var(--ink); }
  .node-title, .core-title {
    font-family: "Saira Semi Condensed", sans-serif; font-weight: 800; fill: var(--green);
  }
  .body-copy { font-family: "Source Serif 4", serif; fill: var(--text); }
  .body-copy .emph { font-style: italic; font-weight: 700; }
  .icon-dark { fill: var(--icon-dark); }
  .icon-people { fill: var(--icon-blue); }
  .icon-store { fill: var(--icon-store); }
</style>
</head>
<body>
<svg class="vision-board" viewBox="0 0 2300 1610" xmlns="http://www.w3.org/2000/svg">
  <defs>
    <path id="arrowhead" d="M0,0 L-30,-14 L-20,0 L-30,14 Z"/>
  </defs>

  <g class="nodes">
    <circle class="node-ring" cx="1185" cy="290" r="228"/>
    <circle class="node-ring" cx="658" cy="608" r="228"/>
    <circle class="node-ring" cx="1697" cy="608" r="228"/>
    <circle class="node-ring" cx="903" cy="1272" r="228"/>
    <circle class="node-ring" cx="1472" cy="1270" r="228"/>
  </g>

  <polygon class="flow-gap" points="1183,368 1600,672 1443,1168 930,1174 768,680"/>
  <g class="flow-rails">
    <line class="flow-rail" x1="1025" y1="456" x2="883" y2="562"/>
    <line class="flow-rail" x1="1070" y1="487" x2="886" y2="620"/>
    <line class="flow-rail" x1="1340" y1="456" x2="1473" y2="555"/>
    <line class="flow-rail" x1="1305" y1="487" x2="1468" y2="612"/>
    <line class="flow-rail" x1="1585" y1="808" x2="1508" y2="1045"/>
    <line class="flow-rail" x1="1545" y1="778" x2="1458" y2="1040"/>
    <line class="flow-rail" x1="1097" y1="1152" x2="1280" y2="1152"/>
    <line class="flow-rail" x1="1118" y1="1193" x2="1253" y2="1193"/>
    <line class="flow-rail" x1="783" y1="800" x2="862" y2="1048"/>
    <line class="flow-rail" x1="822" y1="768" x2="912" y2="1045"/>
  </g>
  <polygon class="flow-path" points="1183,368 1600,672 1443,1168 930,1174 768,680"/>
  <g class="flow-heads">
    <use href="#arrowhead" class="flow-head" transform="translate(928,558) rotate(143)"/>
    <use href="#arrowhead" class="flow-head" transform="translate(862,968) rotate(72)"/>
    <use href="#arrowhead" class="flow-head" transform="translate(1238,1172) rotate(0)"/>
    <use href="#arrowhead" class="flow-head" transform="translate(1538,862) rotate(-72)"/>
    <use href="#arrowhead" class="flow-head" transform="translate(1392,520) rotate(-144)"/>
  </g>

  <line class="note-arrow" x1="885" y1="518" x2="985" y2="447"/>
  <use href="#arrowhead" class="flow-head" transform="translate(1000,437) rotate(-35)"/>
  <text class="body-copy" font-size="27" text-anchor="middle">
    <tspan x="887" y="418">Repeated needs</tspan>
    <tspan x="887" y="451">for some</tspan>
  </text>

  <text class="brand-name" x="1185" y="195" font-size="46" text-anchor="middle">The Larderwell</text>
  <text class="body-copy" font-size="23.5" text-anchor="middle">
    <tspan x="1185" y="258">connects products to nonprofits who are</tspan>
    <tspan x="1185" y="287">serving at-risk populations in a way that</tspan>
    <tspan x="1185" y="316">educates and trains people to be</tspan>
    <tspan x="1185" y="345">self-sustaining.</tspan>
  </text>

  <rect class="icon-dark" x="578" y="405" width="138" height="110" rx="10" role="img" aria-label="Icon of an open hand holding a heart"/>
  <text class="node-title" font-size="38" text-anchor="middle">
    <tspan x="648" y="568">NON PROFIT</tspan>
    <tspan x="648" y="606">ORGANISATION</tspan>
  </text>
  <text class="body-copy" font-size="23.5">
    <tspan x="500" y="636">Non-profit organisations</tspan>
    <tspan x="500" y="665">are connected to each other</tspan>
    <tspan x="500" y="694">and are able to access the</tspan>
    <tspan x="500" y="723">necessary resources from</tspan>
    <tspan x="507" y="753" class="emph">The Larderwell</tspan>
  </text>

  <rect class="icon-store" x="1637" y="438" width="130" height="95" rx="6" role="img" aria-label="Icon of a shopfront with a striped awning"/>
  <text class="node-title" x="1722" y="583" font-size="38" text-anchor="middle">LOCAL BUSINESS</text>
  <text class="body-copy" font-size="25" text-anchor="middle">
    <tspan x="1738" y="625">Local businesses hire</tspan>
    <tspan x="1738" y="656">determined people and in</tspan>
    <tspan x="1738" y="688">tern are able to make</tspan>
    <tspan x="1738" y="719">donations and provide</tspan>
    <tspan x="1738" y="751">volunteers</tspan>
  </text>

  <rect class="icon-people" x="820" y="1192" width="180" height="122" rx="12" role="img" aria-label="Icon of a group of three people"/>
  <text class="body-copy" font-size="23.5" text-anchor="middle">
    <tspan x="908" y="1345">At risk population are able to</tspan>
    <tspan x="908" y="1374">access the resources they</tspan>
    <tspan x="908" y="1403">require because of The</tspan>
    <tspan x="908" y="1432">Larderwell.</tspan>
  </text>

  <rect class="icon-dark" x="1425" y="1130" width="145" height="175" rx="8" role="img" aria-label="Icon of a trainer at a lectern pointing"/>
  <text class="body-copy" font-size="24" text-anchor="middle">
    <tspan x="1482" y="1350" class="emph">Determined people connect to</tspan>
    <tspan x="1482" y="1380">training, mentorship and life</tspan>
    <tspan x="1482" y="1410">coaching</tspan>
  </text>

  <text class="brand-name" x="1185" y="648" font-size="58" text-anchor="middle">The Larderwell</text>
  <text class="core-title" x="1177" y="735" font-size="54" text-anchor="middle">VISION</text>
  <text class="body-copy" font-size="32" text-anchor="middle">
    <tspan x="1197" y="786">To connect resources for low income</tspan>
    <tspan x="1197" y="826">people, nonprofits, and businesses.</tspan>
  </text>
  <text class="core-title" x="1183" y="920" font-size="50" text-anchor="middle">CORE VALUES</text>
  <text class="body-copy" font-size="32" text-anchor="middle">
    <tspan x="1195" y="973">Partnership | Innovation |</tspan>
    <tspan x="1195" y="1013">Connecting | Faith | Community</tspan>
  </text>
</svg>
</body>
</html>
```